Local Flower Farm Needs Business Card Design

I need business cards designed for a flower farm based in Eudora, Kansas.
Business Info:
We are a local cut flower farm located in Eudora, Kansas, founded by Darla Hoffstrom. What started as a passion for agriculture and search for more joy in daily life has blossomed into a small business dedicated to providing the community with beautiful, fresh, and sustainable flowers. We specialize in local, seasonal blooms, ensuring that every petal reflects the care and dedication we pour into our craft. Our mission is to deliver the highest quality flowers directly to our customers through local farmers markets and to florists who share our commitment to sustainability. Join us in celebrating the beauty of nature, one bloom at a time!
Contact Details:
Darla Hoffstrom
Owner
Phone 913-555-0147
Facebook: Lorabelle Quinn Blossoms
Instagram: @LorabelleQuinnBlossoms
Website: LorabelleQuinnBlossoms.example
Target Market(s)
Wholesale to Florists and Direct to Consumer via Farmers Market
Industry/Entity Type
Florist, Farm
Contact Information for Business Card
Name, Contact Info, Logo
Look and feel

```html
<!DOCTYPE html>
<html lang="en">
<head>
<meta charset="utf-8">
<title>Lorabelle Quinn Blossoms – Business Card</title>
<link rel="stylesheet" href="https://fonts.googleapis.com/css2?family=Montserrat:wght@400;700&display=swap">
<style>
  :root {
    --ink: #0a2830;
    --card-dark: #08222a;
    --paper: #f3f3f3;
    --stage: #e4e6e5;
    --on-dark: #e6e8e7;
  }
  * { box-sizing: border-box; margin: 0; padding: 0; }
  html, body { width: 1200px; height: 1200px; overflow: hidden; }
  body {
    background: var(--stage);
    font-family: "Montserrat", Arial, sans-serif;
    color: var(--ink);
    display: flex;
    flex-direction: column;
    align-items: center;
    justify-content: center;
    gap: 42px;
  }
  .card {
    position: relative;
    width: 900px;
    height: 514px;
    border-radius: 5px;
    box-shadow: 0 10px 30px rgba(0,0,0,.12);
  }
  .card--front { background: var(--paper); }
  .card--back { background: var(--card-dark); color: var(--on-dark); }

  .holder { position: absolute; left: 73px; top: 74px; }
  .holder__name { font-size: 31px; font-weight: 700; line-height: 1.1; }
  .holder__role { font-size: 23px; font-weight: 400; margin-top: 2px; }

  .contact-row {
    display: flex; align-items: center; gap: 12px;
    font-size: 23px; font-weight: 400; white-space: nowrap;
  }
  .contact-row--phone { position: absolute; right: 73px; top: 90px; }
  .contact-list {
    position: absolute; left: 73px; top: 330px;
    display: flex; flex-direction: column; gap: 12px;
  }
  .icon { width: 28px; height: 28px; flex: none; }

  .brand-mark {
    position: absolute; right: 30px; bottom: 40px;
    font-size: 22px; font-weight: 700; line-height: 1.25;
    text-align: right; text-transform: uppercase; letter-spacing: 2px;
    color: var(--ink);
  }

  .seal {
    position: absolute; left: 50%; top: 257px;
    width: 276px; height: 276px; transform: translate(-50%, -50%);
    border: 1.5px solid var(--on-dark); border-radius: 50%;
    display: flex; align-items: center; justify-content: center;
    text-align: center;
    font-size: 22px; font-weight: 400; letter-spacing: 3px;
    text-transform: uppercase; line-height: 1.45;
  }
  .social-handle {
    position: absolute; left: 0; right: 0; top: 436px;
    justify-content: center; color: var(--on-dark);
  }
</style>
</head>
<body>
  <section class="card card--front" aria-label="Business card front">
    <div class="holder">
      <p class="holder__name">Darla Hoffstrom</p>
      <p class="holder__role">Owner</p>
    </div>

    <p class="contact-row contact-row--phone">
      <svg class="icon" viewBox="0 0 28 28" aria-hidden="true">
        <circle cx="14" cy="14" r="14" fill="var(--ink)"/>
        <path d="M10 8c.8 0 1.6 2.3 1.6 3 0 .7-1 1-1 1.6.4 1.6 2 3.2 3.6 3.6.6 0 .9-1 1.6-1 .7 0 3 .8 3 1.6 0 1.2-1.2 2.2-2.4 2.2C12.5 19 9 15.5 8 11.4 7.8 9.2 8.8 8 10 8z" fill="#fff"/>
      </svg>
      913-555-0147
    </p>

    <div class="contact-list">
      <p class="contact-row">
        <svg class="icon" viewBox="0 0 28 28" aria-hidden="true">
          <circle cx="14" cy="14" r="14" fill="var(--ink)"/>
          <rect x="8" y="9.5" width="12" height="9" rx="1.2" fill="#fff"/>
          <path d="M8.5 10.5 14 14.6l5.5-4.1" stroke="var(--ink)" stroke-width="1.4" fill="none"/>
        </svg>
        darla@lorabellequinnblossoms.example
      </p>
      <p class="contact-row">
        <svg class="icon" viewBox="0 0 28 28" aria-hidden="true">
          <circle cx="14" cy="14" r="14" fill="var(--ink)"/>
          <circle cx="14" cy="14" r="7" fill="none" stroke="#fff" stroke-width="1.5"/>
          <ellipse cx="14" cy="14" rx="3" ry="7" fill="none" stroke="#fff" stroke-width="1.3"/>
          <path d="M7 14h14" stroke="#fff" stroke-width="1.3"/>
        </svg>
        www.lorabellequinnblossoms.example
      </p>
      <p class="contact-row">
        <svg class="icon" viewBox="0 0 28 28" aria-hidden="true">
          <circle cx="14" cy="14" r="14" fill="var(--ink)"/>
        </svg>
        @LorabelleQuinnBlossoms
      </p>
    </div>

    <p class="brand-mark">Lorabelle<br>Quinn<br>Blossoms</p>
  </section>

  <section class="card card--back" aria-label="Business card back">
    <div class="seal">
      <p>Lorabelle<br>Quinn<br>Blossoms</p>
    </div>
    <p class="contact-row social-handle">
      <svg class="icon" viewBox="0 0 28 28" aria-hidden="true">
        <circle cx="14" cy="14" r="14" fill="var(--on-dark)"/>
      </svg>
      @LorabelleQuinnBlossoms
    </p>
  </section>
</body>
</html>
```